Design a Website for an IT Support Company

We are an IT support company that provides commercial IT support and services to small and medium sized businesses. We are in need of a website to be developed for our business.
We would like to work with someone who is either familiar with the IT field, or has developed a website for an IT support company in the past.
Some examples of designs/layouts that we like:
https://www.velmorask.example/
http://www.quibenstack.example/
http://572zo.example/
http://www.guspelnetworks.example/
http://www.ourba.example/
I have attached a word document that gives a menu system/page layout format that we would like for our website as well as branch office phone numbers. Our logo is also attached that you can use for your design purposes. We currently do not have copy produced for all of the pages outlined in the word document, but would get this done during the project with the selected designer.
We would like the website to be SEO friendly & fully responsive. We would prefer a Wordpress format, however, we are open to HTML formats as well.

```html
<!DOCTYPE html>
<html lang="en">
<head>
<meta charset="utf-8">
<title>Nimbrel IT – Commercial IT Support and Services</title>
<link rel="stylesheet" href="https://fonts.googleapis.com/css2?family=Roboto+Condensed:wght@400;700&family=Roboto:wght@400;500;700&display=swap">
<style>
:root{
  --blue:#0b72bb;
  --blue-bright:#1b9ae4;
  --navy:#0c4e80;
  --navy-deep:#08385f;
  --ink:#333;
  --muted:#888;
  --line:#e2e2e2;
  --icon:#5a6a78;
  --header-bg:#f6f6f6;
  --white:#fff;
}
*{box-sizing:border-box;margin:0;padding:0}
html,body{width:1200px;height:3056px;overflow:hidden}
body{font-family:"Roboto",Arial,sans-serif;color:var(--ink);background:var(--white);position:relative}
.cond{font-family:"Roboto Condensed","Arial Narrow",sans-serif}
.container{width:700px;margin:0 auto;position:relative}
h2.section-title{font-family:"Roboto Condensed","Arial Narrow",sans-serif;font-weight:700;font-size:23px;text-align:center;color:#222;text-transform:uppercase}
h2.section-title .accent{color:var(--blue)}

/* header */
.site-header{height:92px;background:var(--header-bg)}
.site-header .container{display:flex;align-items:center;height:92px}
.brand{display:flex;align-items:center;gap:10px;font-family:"Roboto Condensed",sans-serif;font-weight:700;font-size:26px;color:#1d3a57}
.brand-dot{width:26px;height:26px;border-radius:50%;background:var(--blue)}
.main-nav{display:flex;gap:20px;margin-left:52px;font-family:"Roboto Condensed",sans-serif;font-size:11px;text-transform:uppercase}
.main-nav a{color:var(--blue);text-decoration:none;padding:4px 0}
.main-nav a.active{background:var(--blue);color:#fff;padding:4px 10px;border-radius:2px}
.header-phone{margin-left:auto;display:flex;align-items:center;gap:6px;font-family:"Roboto Condensed",sans-serif;font-size:12px;color:#222}
.header-phone b{color:var(--blue);font-weight:700}

/* hero */
.hero{height:454px;position:relative;background:linear-gradient(180deg,#17365a 0%,#1f4f7e 45%,#142f52 100%);color:#fff;text-align:center}
.hero-photo{position:absolute;inset:0;background:radial-gradient(ellipse at 50% 55%,rgba(70,120,170,.55),rgba(10,30,60,0) 60%)}
.hero-eyebrow{position:absolute;top:204px;left:0;right:0;font-family:"Roboto Condensed",sans-serif;font-weight:700;font-size:15px;letter-spacing:.3px}
.hero-title{position:absolute;top:228px;left:0;right:0;font-family:"Roboto Condensed",sans-serif;font-weight:700;font-size:31px}
.hero-dots{position:absolute;top:400px;left:0;right:0;display:flex;justify-content:center;gap:4px}
.hero-dots span{width:9px;height:9px;border-radius:50%;border:1.5px solid #fff}
.hero-dots span.on{background:var(--blue-bright);border-color:var(--blue-bright)}

/* services */
.services{height:444px;padding-top:38px}
.service-cards{display:flex;gap:18px;margin-top:22px;justify-content:center}
.service-card{width:221px;height:310px;border:1px solid var(--line);text-align:center;position:relative}
.service-card .photo{height:178px}
.service-card .badge{position:absolute;top:136px;left:50%;margin-left:-42px;width:84px;height:84px;border-radius:50%;background:#e9ecef;border:4px solid #fff;display:flex;align-items:center;justify-content:center}
.service-card h3{margin-top:56px;font-family:"Roboto Condensed",sans-serif;font-size:11px;color:var(--blue);text-transform:uppercase}
.service-card p{font-size:9.5px;line-height:15px;color:var(--muted);margin:8px 22px 0}

/* about */
.about{height:383px;background:radial-gradient(ellipse at 50% 40%,#166aa3 0%,var(--navy) 55%,var(--navy-deep) 100%);color:#fff;text-align:center;padding-top:56px}
.about h2{font-family:"Roboto Condensed",sans-serif;font-size:23px;font-weight:700}
.about h2 .accent{color:#33b5f5}
.about p{width:630px;margin:28px auto 0;font-size:9.5px;line-height:20px}
.about p + p{margin-top:14px}
.btn{display:inline-block;margin-top:30px;width:102px;height:26px;line-height:26px;background:var(--blue);color:#fff;font-family:"Roboto Condensed",sans-serif;font-size:10px;font-weight:700;text-transform:uppercase}

/* overview */
.overview{height:811px;background:linear-gradient(180deg,#f9f9f9,#fff 40%,#f4f5f6);padding-top:73px}
.divider{width:120px;height:2px;background:#ccc;margin:0 auto;position:relative}
.divider::after{content:"";position:absolute;left:46px;top:-2px;width:28px;height:6px;border-radius:3px;background:#999}
.overview h2{margin-top:22px}
.icon-grid{display:grid;grid-template-columns:repeat(5,146px);justify-content:center;margin:36px auto 0;row-gap:28px}
.icon-item{text-align:center;font-family:"Roboto Condensed",sans-serif;font-size:10px;text-transform:uppercase;color:#333}
.icon-item svg{display:block;margin:0 auto 8px}
.overview .block{margin-top:48px}

/* testimonials */
.testimonials{height:313px;background:radial-gradient(ellipse at 50% 40%,#146aa4 0%,var(--navy) 60%,var(--navy-deep) 100%);color:#fff;text-align:center;padding-top:52px;position:relative}
.testimonials h2{font-family:"Roboto Condensed",sans-serif;font-size:22px;font-weight:700}
.avatars{display:flex;justify-content:center;align-items:center;gap:8px;margin-top:18px}
.avatar{width:32px;height:32px;border-radius:50%;background:#8fb3d1;border:2px solid #cfe0ee}
.avatar.main{width:44px;height:44px;background:#c9d6e2;border-color:#fff}
.quote{width:560px;margin:12px auto 0;font-size:9.5px;line-height:14px}
.quote-dash{width:14px;height:1px;background:#fff;margin:12px auto 0}
.author{margin-top:12px;font-family:"Roboto Condensed",sans-serif;font-weight:700;font-size:10px;text-transform:uppercase}
.author-co{font-size:9px;color:#cfe0ee;margin-top:3px}
.quote-next{position:absolute;left:876px;top:196px}

/* partners */
.partners{height:245px;padding-top:58px}
.partner-row{display:flex;justify-content:space-between;align-items:center;margin-top:70px}
.partner{display:flex;align-items:center;gap:7px;font-family:"Roboto Condensed",sans-serif;font-size:17px;color:#666}
.partner i{width:20px;height:20px;background:#888;display:block}
.partner i.round{border-radius:50%}

/* footer */
.site-footer{height:314px;background:var(--navy);color:#fff;padding-top:50px}
.footer-cols{display:flex}
.footer-col{width:238px}
.footer-col h4{font-family:"Roboto Condensed",sans-serif;font-size:20px;font-weight:700;text-transform:uppercase;margin-bottom:14px}
.footer-col ul{list-style:none;font-size:9px;line-height:22px}
.socials{display:flex;gap:4px}
.socials span{width:17px;height:17px;background:#2d8fd6;border-radius:2px}
.seal{margin-top:20px;width:104px;height:40px;border-radius:4px;background:#fff;display:flex;align-items:center;padding-left:6px}
.seal span{width:26px;height:30px;background:var(--blue);border-radius:3px}
.footer-bottom{position:absolute;left:250px;right:250px;top:3006px;border-top:1px solid #2f6a97;text-align:center;font-size:8.5px;padding-top:18px}
</style>
</head>
<body>

<header class="site-header">
  <div class="container">
    <div class="brand"><span class="brand-dot"></span>Nimbrel IT</div>
    <nav class="main-nav">
      <a class="active">Home</a><a>Services</a><a>Why Nimbrel IT</a><a>Contact</a>
    </nav>
    <div class="header-phone">
      <svg width="12" height="12" viewBox="0 0 24 24"><path fill="#222" d="M6.6 10.8a15 15 0 0 0 6.6 6.6l2.2-2.2c.3-.3.7-.4 1-.2 1.1.4 2.3.6 3.6.6.6 0 1 .4 1 1V20c0 .6-.4 1-1 1A17 17 0 0 1 3 4c0-.6.4-1 1-1h3.5c.6 0 1 .4 1 1 0 1.3.2 2.5.6 3.6.1.3 0 .7-.2 1z"/></svg>
      <b>MAIN NUMBER:</b> 555-310-4400
    </div>
  </div>
</header>

<section class="hero">
  <div class="hero-photo" role="img" aria-label="Technician working on a laptop in a server room aisle, blue tones"></div>
  <div class="hero-eyebrow">WE ARE YOUR IT DEPARTMENT</div>
  <h1 class="hero-title">COMMERCIAL IT SUPPORT AND SERVICES</h1>
  <div class="hero-dots"><span class="on"></span><span></span><span></span></div>
</section>

<section class="services">
  <h2 class="section-title"><span class="accent">Nimbrel IT</span> Services</h2>
  <div class="service-cards">
    <article class="service-card">
      <div class="photo" role="img" aria-label="Two colleagues reviewing work at a laptop in a bright office" style="background:linear-gradient(135deg,#e8e4df,#c9b8a6)"></div>
      <div class="badge"><svg width="36" height="36" viewBox="0 0 36 36"><circle cx="20" cy="15" r="9" fill="none" stroke="#1b7fc4" stroke-width="3"/><path d="M13 22 5 30" stroke="#1b7fc4" stroke-width="4" stroke-linecap="round"/></svg></div>
      <h3>Data Services</h3>
      <p>Lorem ipsum dolor sit amet, consectetur adipiscing elit. Nulla nec porttitor justo.</p>
    </article>
    <article class="service-card">
      <div class="photo" role="img" aria-label="Hands holding a tablet with glowing cloud data graphics" style="background:linear-gradient(135deg,#1d2c3e,#4a7fa8)"></div>
      <div class="badge"><svg width="38" height="36" viewBox="0 0 38 36"><path d="M10 22a6 6 0 0 1 1-12 8 8 0 0 1 15 2 5 5 0 0 1 1 10z" fill="none" stroke="#5a6a78" stroke-width="2"/><path d="M19 22v8M13 30h12" stroke="#1b7fc4" stroke-width="2"/></svg></div>
      <h3>Cloud Services</h3>
      <p>Lorem ipsum dolor sit amet, consectetur adipiscing elit. Nulla nec porttitor justo.</p>
    </article>
    <article class="service-card">
      <div class="photo" role="img" aria-label="Support staff wearing headsets at a call desk" style="background:linear-gradient(135deg,#f1ede9,#b9a593)"></div>
      <div class="badge"><svg width="36" height="36" viewBox="0 0 36 36"><path d="M8 20v-3a10 10 0 0 1 20 0v3" fill="none" stroke="#5a6a78" stroke-width="3"/><rect x="5" y="19" width="6" height="9" rx="2" fill="#1b7fc4"/><rect x="25" y="19" width="6" height="9" rx="2" fill="#1b7fc4"/></svg></div>
      <h3>Voice Services</h3>
      <p>Lorem ipsum dolor sit amet, consectetur adipiscing elit. Nulla nec porttitor justo.</p>
    </article>
  </div>
</section>

<section class="about">
  <h2>ABOUT <span class="accent">&nbsp;NIMBREL IT</span></h2>
  <p>Lorem ipsum dolor sit amet, consectetur adipiscing elit. Praesent mollis pellentesque nunc sed ornare. In auctor lectus non ornare imperdiet. Fusce sed fermentum lorem, sit amet ullamcorper sem. Phasellus ex felis, sagittis id egestas id, iaculis sed augue. Suspendisse eget pulvinar lorem, eget efficitur ligula. In lorem risus, viverra vel turpis eget, consectetur accumsan ligula. Nulla id luctus ex. Donec laoreet metus maximus, tempus ipsum eu, ultricies sem. Suspendisse at arcu ligula. Fusce pulvinar, diam a egestas finibus, urna mollis tellus, id bibendum tortor leo a mi.</p>
  <p>Nullam tempor, erat ut iaculis porta, leo odio ullamcorper libero, vitae mattis nisl tellus sit amet sed. Nulla non faucibus urna. Maecenas pretium diam non mi egestas consequat.</p>
  <a class="btn">Read More</a>
</section>

<section class="overview">
  <div class="block-first">
    <div class="divider"></div>
    <h2 class="section-title"><span class="accent">Data Services</span> Overview</h2>
    <div class="icon-grid">
      <div class="icon-item"><svg width="30" height="26" viewBox="0 0 30 26"><rect x="10" y="1" width="10" height="7" fill="#5a6a78"/><rect x="1" y="17" width="10" height="7" fill="#5a6a78"/><rect x="19" y="17" width="10" height="7" fill="#5a6a78"/><path d="M15 8v5M6 13h18M6 13v4M24 13v4" stroke="#5a6a78" stroke-width="2" fill="none"/></svg>Managed IT Services</div>
      <div class="icon-item"><svg width="30" height="26" viewBox="0 0 30 26"><circle cx="15" cy="6" r="4" fill="#1b7fc4"/><circle cx="6" cy="14" r="3" fill="#5a6a78"/><circle cx="24" cy="14" r="3" fill="#5a6a78"/><path d="M1 25a5 5 0 0 1 10 0M19 25a5 5 0 0 1 10 0" fill="#5a6a78"/></svg>IT Support &amp; Consultin</div>
      <div class="icon-item"><svg width="30" height="26" viewBox="0 0 30 26"><rect x="2" y="2" width="20" height="15" fill="none" stroke="#5a6a78" stroke-width="2"/><rect x="23" y="4" width="5" height="20" fill="#5a6a78"/><path d="M8 23h10M12 17v6" stroke="#5a6a78" stroke-width="2"/></svg>IT Helpdesk Services</div>
      <div class="icon-item"><svg width="30" height="26" viewBox="0 0 30 26"><rect x="9" y="11" width="12" height="11" fill="#1b7fc4"/><path d="M11 11V7a4 4 0 0 1 8 0v4" fill="none" stroke="#5a6a78" stroke-width="2"/><path d="M3 8h4M23 8h4M3 18h4M23 18h4" stroke="#5a6a78" stroke-width="2"/></svg>Network Security</div>
      <div class="icon-item"><svg width="30" height="26" viewBox="0 0 30 26"><path d="M8 14a5 5 0 0 1 1-10 7 7 0 0 1 13 2 4 4 0 0 1 0 8z" fill="#5a6a78"/><path d="M11 16v8M8 21l3 3 3-3M19 24v-8M16 19l3-3 3 3" stroke="#1b7fc4" stroke-width="2" fill="none"/></svg>Data Backup &amp; Recovery</div>
      <div class="icon-item"><svg width="30" height="26" viewBox="0 0 30 26"><path d="M7 13a5 5 0 0 1 1-10 7 7 0 0 1 13 2 4 4 0 0 1 0 8z" fill="#1b7fc4"/><rect x="3" y="15" width="14" height="4" fill="#5a6a78"/><rect x="3" y="20" width="14" height="4" fill="#5a6a78"/><rect x="19" y="17" width="9" height="6" fill="#5a6a78"/></svg>Servers &amp; Virtualization</div>
      <div class="icon-item"><svg width="30" height="26" viewBox="0 0 30 26"><rect x="4" y="2" width="22" height="15" fill="none" stroke="#5a6a78" stroke-width="2"/><path d="M8 12l4-4 3 3 5-5" stroke="#1b7fc4" stroke-width="2" fill="none"/><path d="M15 17v6M9 24h12" stroke="#5a6a78" stroke-width="2"/></svg>Remote Monitoring Services</div>
      <div class="icon-item"><svg width="30" height="26" viewBox="0 0 30 26"><rect x="3" y="16" width="24" height="7" rx="2" fill="#5a6a78"/><path d="M15 16V8M10 6a7 7 0 0 1 10 0M7 3a11 11 0 0 1 16 0" stroke="#1b7fc4" stroke-width="2" fill="none"/></svg>Wireless Networking</div>
      <div class="icon-item"><svg width="30" height="26" viewBox="0 0 30 26"><rect x="2" y="5" width="22" height="15" fill="none" stroke="#5a6a78" stroke-width="2"/><path d="M2 5l11 8 11-8" stroke="#5a6a78" stroke-width="2" fill="none"/><circle cx="24" cy="19" r="5" fill="#1b7fc4"/></svg>Email &amp; Spam Threat Management</div>
      <div class="icon-item"><svg width="30" height="26" viewBox="0 0 30 26"><circle cx="9" cy="8" r="5" fill="none" stroke="#5a6a78" stroke-width="2"/><circle cx="21" cy="18" r="5" fill="none" stroke="#1b7fc4" stroke-width="2"/><path d="M13 11l4 4" stroke="#5a6a78" stroke-width="2"/></svg>Structured Cabling</div>
    </div>
  </div>

  <div class="block">
    <div class="divider"></div>
    <h2 class="section-title"><span class="accent">Cloud Services</span> Overview</h2>
    <div class="icon-grid">
      <div class="icon-item"><svg width="30" height="26" viewBox="0 0 30 26"><rect x="8" y="3" width="14" height="20" fill="#5a6a78"/><rect x="11" y="6" width="8" height="14" fill="#fff"/></svg>Workdesk 365 Migrations</div>
      <div class="icon-item"><svg width="30" height="26" viewBox="0 0 30 26"><circle cx="8" cy="8" r="4" fill="#5a6a78"/><circle cx="22" cy="8" r="4" fill="#1b7fc4"/><circle cx="15" cy="19" r="4" fill="#5a6a78"/><path d="M8 8l7 11 7-11" stroke="#5a6a78" fill="none"/></svg>Amberline Cloud Management Services</div>
      <div class="icon-item"><svg width="30" height="26" viewBox="0 0 30 26"><path d="M8 15a5 5 0 0 1 1-10 7 7 0 0 1 13 2 4 4 0 0 1 0 8z" fill="none" stroke="#5a6a78" stroke-width="2"/><path d="M15 15v8M11 19l4 4 4-4" stroke="#1b7fc4" stroke-width="2" fill="none"/></svg>Cloud Migration Services</div>
      <div class="icon-item"><svg width="30" height="26" viewBox="0 0 30 26"><circle cx="15" cy="13" r="10" fill="#5a6a78"/><path d="M5 13h20M15 3c4 4 4 16 0 20" stroke="#fff" stroke-width="1.5" fill="none"/></svg>Hosted Virtual Servers</div>
      <div class="icon-item"><svg width="30" height="26" viewBox="0 0 30 26"><rect x="5" y="3" width="20" height="13" fill="#5a6a78"/><rect x="2" y="18" width="26" height="4" fill="#1b7fc4"/></svg>Hosted Telephone Systems</div>
    </div>
  </div>

  <div class="block">
    <div class="divider"></div>
    <h2 class="section-title"><span class="accent">Cloud Services</span> Overview</h2>
    <div class="icon-grid">
      <div class="icon-item"><svg width="30" height="26" viewBox="0 0 30 26"><circle cx="15" cy="13" r="11" fill="none" stroke="#5a6a78" stroke-width="2"/><path d="M15 6v14M9 9l12 8M21 9 9 17" stroke="#1b7fc4" stroke-width="2"/></svg>Astrelle Consulting</div>
      <div class="icon-item"><svg width="30" height="26" viewBox="0 0 30 26"><rect x="6" y="2" width="18" height="22" rx="2" fill="#5a6a78"/><rect x="9" y="5" width="12" height="5" fill="#fff"/><path d="M10 14h2M14 14h2M18 14h2M10 18h2M14 18h2M18 18h2" stroke="#fff" stroke-width="2"/></svg>Business Telephone</div>
      <div class="icon-item"><svg width="30" height="26" viewBox="0 0 30 26"><rect x="3" y="6" width="7" height="18" fill="#5a6a78"/><rect x="11" y="2" width="8" height="22" fill="#1b7fc4"/><rect x="20" y="8" width="7" height="16" fill="#5a6a78"/></svg>Multiple Office Phone</div>
      <div class="icon-item"><svg width="30" height="26" viewBox="0 0 30 26"><path d="M8 14a5 5 0 0 1 1-10 7 7 0 0 1 13 2 4 4 0 0 1 0 8z" fill="#1b7fc4"/><rect x="10" y="15" width="10" height="9" fill="#5a6a78"/></svg>Granmoor Telephone</div>
      <div class="icon-item"><svg width="30" height="26" viewBox="0 0 30 26"><rect x="9" y="2" width="12" height="22" rx="2" fill="#5a6a78"/><rect x="11" y="5" width="8" height="6" fill="#1b7fc4"/><rect x="4" y="14" width="4" height="10" fill="#1b7fc4"/></svg>SIP Trunks</div>
    </div>
  </div>
</section>

<section class="testimonials">
  <h2>TESTIMONIALS</h2>
  <div class="avatars">
    <div class="avatar" role="img" aria-label="Client portrait thumbnail"></div>
    <div class="avatar main" role="img" aria-label="Portrait of the quoted client"></div>
    <div class="avatar" role="img" aria-label="Client portrait thumbnail"></div>
  </div>
  <p class="quote">Lorem ipsum dolor sit amet, consectetur adipiscing elit. Donec maximus sodales tristique. Nulla vitae dui vitae nibh commodo scelerisque sed id lacus. Donec faucibus diam tellus, at maximus nunc dictum at. Phasellus sollicitudin tortor vitae ultrices viverra. Nullam lacus ex, finibus eget interdum nec, elementum ac enim. Nulla facilisi. Nunc dapibus dapibus placerat.</p>
  <div class="quote-dash"></div>
  <div class="author">Dale Fenwick</div>
  <div class="author-co">Brightpath Training Co.</div>
  <svg class="quote-next" width="18" height="12" viewBox="0 0 18 12"><circle cx="6" cy="6" r="4" fill="none" stroke="#fff" stroke-width="1.3"/><circle cx="12" cy="6" r="4" fill="none" stroke="#fff" stroke-width="1.3"/></svg>
</section>

<section class="partners">
  <div class="container">
    <h2 class="section-title"><span class="accent">Technology</span> Partners</h2>
    <div class="partner-row">
      <div class="partner"><i></i>Kerrowin</div>
      <div class="partner"><i class="round"></i>Dalvey</div>
      <div class="partner">Sorvik</div>
      <div class="partner">Amberline Cloud</div>
      <div class="partner"><i class="round"></i>Astrelle</div>
      <div class="partner"><i></i>Workdesk 365</div>
    </div>
  </div>
</section>

<footer class="site-footer">
  <div class="container">
    <div class="footer-cols">
      <div class="footer-col">
        <h4>Quick Contact</h4>
        <ul>
          <li>Houston: 555-201-3300</li>
          <li>San Antonio: 555-202-4700</li>
          <li>Austin: 555-203-9000</li>
          <li>Tulsa: 555-204-0030</li>
          <li>Oklahoma City: 555-205-9009</li>
        </ul>
      </div>
      <div class="footer-col">
        <h4>Navigation</h4>
        <ul>
          <li>Home</li><li>about us</li><li>Why Nimbrel IT</li><li>Locations</li><li>Terms and Conditions</li><li>Privacy Policy</li><li>Contact us</li>
        </ul>
      </div>
      <div class="footer-col">
        <h4>Stay Connected</h4>
        <div class="socials"><span></span><span></span><span></span><span></span><span></span><span></span></div>
        <div class="seal"><span></span></div>
      </div>
    </div>
  </div>
  <div class="footer-bottom">Copyright © 2017 Nimbrel IT</div>
</footer>

</body>
</html>
```